Business Card Design Project

Automotive (vehcle imports & servicing, repairs)business card needed. professional & sleek look needed.

colours same as logo colours pref.

prefer to have few performance logos and Brand names on the card as well.

Target Market(s)

prestige car imports
automotive repairs & service
Automotive compliance workshop

Industry/Entity Type

Automotive

Requirements
Must have
• car brand logos
company details
logo
web address
contact details

```html
<!DOCTYPE html>
<html lang="en">
<head>
<meta charset="utf-8">
<title>Torque Harbour — Business Card</title>
<link rel="stylesheet" href="https://fonts.googleapis.com/css2?family=Michroma&display=swap">
<style>
  :root {
    --page-bg: #e8e5e1;
    --red: #e3151f;
    --red-deep: #b80d16;
    --black: #111111;
    --white: #ffffff;
    --silver-light: #e4e5e7;
    --silver-mid: #c3c5c8;
    --silver-dark: #8d9095;
    --badge-text: #3a3c40;
    --edge-line: #2b2c2f;
  }
  html, body {
    margin: 0;
    width: 1200px;
    height: 800px;
    overflow: hidden;
    background: var(--page-bg);
    font-family: "Michroma", sans-serif;
  }
  .business-card {
    position: absolute;
    left: 150px;
    top: 140px;
    width: 900px;
    height: 520px;
    border-radius: 10px;
    overflow: hidden;
    background: linear-gradient(160deg, var(--red) 0%, var(--red) 55%, var(--red-deep) 100%);
    box-shadow: 0 10px 30px rgba(0,0,0,0.18);
  }
  .card-base {
    position: absolute;
    inset: 0;
  }
  .brand-block {
    position: absolute;
    left: 200px;
    top: 70px;
  }
  .wordmark {
    margin: 0;
    color: var(--white);
    font-weight: 400;
    font-size: 62px;
    line-height: 1.08;
    letter-spacing: 1px;
  }
  .tagline {
    margin: 14px 0 0 4px;
    color: var(--black);
    font-size: 15px;
    letter-spacing: 2px;
  }
  .tagline .dot {
    display: inline-block;
    width: 8px;
    height: 8px;
    border-radius: 50%;
    background: var(--white);
    margin: 0 10px;
    vertical-align: middle;
  }
  .web-address {
    margin: 12px 0 0 120px;
    color: var(--white);
    font-size: 24px;
    letter-spacing: 6px;
  }
  .make-row {
    position: absolute;
    left: 40px;
    right: 30px;
    bottom: 28px;
    display: flex;
    justify-content: space-between;
    align-items: center;
    margin: 0;
    padding: 0;
    list-style: none;
  }
  .make-badge {
    display: flex;
    align-items: center;
    gap: 8px;
    color: var(--badge-text);
    font-size: 12px;
    letter-spacing: 1px;
    white-space: nowrap;
  }
  .make-badge::before {
    content: "";
    width: 14px;
    height: 14px;
    border-radius: 50%;
    background: var(--silver-dark);
  }
</style>
</head>
<body>
  <article class="business-card">
    <svg class="card-base" width="900" height="520" viewBox="0 0 900 520" aria-hidden="true">
      <defs>
        <linearGradient id="silverPlate" x1="0" y1="0" x2="0" y2="1">
          <stop offset="0" stop-color="var(--silver-light)"/>
          <stop offset="0.5" stop-color="var(--silver-mid)"/>
          <stop offset="1" stop-color="var(--silver-light)"/>
        </linearGradient>
      </defs>
      <path d="M0 420 L520 420 C600 420 640 330 720 320 L900 305 L900 520 L0 520 Z"
            fill="url(#silverPlate)"/>
      <path d="M0 420 L520 420 C600 420 640 330 720 320 L900 305"
            fill="none" stroke="var(--edge-line)" stroke-width="5"/>
      <path d="M0 412 L516 412 C596 412 636 322 716 312 L900 297"
            fill="none" stroke="var(--white)" stroke-opacity="0.35" stroke-width="2"/>
    </svg>

    <div class="brand-block">
      <h1 class="wordmark">TORQUE<br>HARBOUR</h1>
      <p class="tagline">PRESTIGE<span class="dot"></span>PERFORMANCE<span class="dot"></span>MUSCLE</p>
      <p class="web-address">torqueharbour.com.au</p>
    </div>

    <ul class="make-row">
      <li class="make-badge">Ridgeline Cycles</li>
      <li class="make-badge">Corsaro</li>
      <li class="make-badge">Kanemura</li>
      <li class="make-badge">Ashford Vane</li>
      <li class="make-badge">Tridenza</li>
      <li class="make-badge">Sanryo</li>
    </ul>
  </article>
</body>
</html>
```